A5 Flyer for Financial Services Business

I am after a re-design of our business flyer to fit in with our new branding style and logo colour scheme. Wanting something with a bit of designer flair that I could not create myself. I have included the flyer which I created which lacks style so dazzle me.

I want to use the same content.

Text for main body of flyer is

Are you a small business owner, tradie or PAVC Service Provider struggling to stay on top of your bookkeeping and compliance obligations? If so we would love to help you get back on track and take control of your business finances so that you can make informed business decisions and focus on what you do best.

We have over 20 years industry experience and, as a small business ourselves, we are able to offer our clients a personal bookkeeping solution tailored to meet the needs of your business.

Accounts Payable | Accounts Receivable
Customer Invoicing
Bank and Credit Card Reconciliations
Payroll | Superannuation | Payroll Tax
Business Activity | Instalment Activity Statements
Regular Financial Reports
Ledgerly and Bookwise Set-Up and Training

```html
<!DOCTYPE html>
<html lang="en">
<head>
<meta charset="utf-8">
<title>Even Keel Financial Services – A5 Flyer</title>
<link rel="stylesheet" href="https://fonts.googleapis.com/css2?family=Montserrat:wght@400;700;800&display=swap">
<style>
  :root {
    --page-bg: #e4e5e6;
    --navy: #0c3a58;
    --teal-top: #0f3f5c;
    --teal-bottom: #17968f;
    --photo-dark: #0b2542;
    --photo-light: #2c5f8e;
    --silver-dark: #8a8d91;
    --silver-light: #f2f2f3;
    --ring: #17968f;
    --white: #ffffff;
  }
  * { margin: 0; padding: 0; box-sizing: border-box; }
  html, body {
    width: 1200px;
    height: 965px;
    overflow: hidden;
    background: var(--page-bg);
    font-family: "Montserrat", Arial, sans-serif;
  }
  .flyer {
    position: absolute;
    left: 284px;
    top: 32px;
    width: 632px;
    height: 900px;
    background: var(--white);
    overflow: hidden;
    box-shadow: 0 6px 24px rgba(0,0,0,0.18);
  }
  .flyer-shapes {
    position: absolute;
    inset: 0;
    width: 632px;
    height: 900px;
  }
  .brand {
    position: absolute;
    left: 40px;
    top: 62px;
    width: 290px;
    text-align: center;
    color: var(--white);
    font-weight: 400;
  }
  .brand-name {
    font-size: 30px;
    letter-spacing: 1px;
    line-height: 1.1;
  }
  .brand-tagline {
    font-size: 18px;
    letter-spacing: 6px;
    line-height: 1.2;
  }
  .headline {
    position: absolute;
    left: 134px;
    top: 150px;
    color: var(--white);
    font-weight: 800;
    text-shadow: 2px 3px 4px rgba(0,0,0,0.55);
    line-height: 1;
  }
  .headline span { display: block; }
  .headline .big { font-size: 58px; letter-spacing: -1px; }
  .headline .small { font-size: 36px; margin: 12px 0 10px; }
  .intro {
    position: absolute;
    right: 376px;
    top: 346px;
    text-align: right;
    white-space: nowrap;
    color: var(--white);
    font-weight: 700;
    font-size: 17.5px;
    line-height: 35.4px;
  }
  .services {
    position: absolute;
    left: 290px;
    top: 500px;
    list-style: none;
  }
  .services li {
    position: relative;
    padding-left: 20px;
    height: 36.8px;
    line-height: 22px;
    font-size: 12px;
    letter-spacing: -0.1px;
    font-weight: 700;
    color: var(--navy);
    white-space: nowrap;
  }
  .services li::before {
    content: "";
    position: absolute;
    left: 0;
    top: 4px;
    width: 14px;
    height: 14px;
    border: 3px solid var(--ring);
    border-radius: 50%;
  }
</style>
</head>
<body>
  <main class="flyer">
    <svg class="flyer-shapes" viewBox="0 0 632 900">
      <defs>
        <linearGradient id="side-panel-fill" x1="0" y1="0" x2="0" y2="1">
          <stop offset="0" stop-color="var(--teal-top)"/>
          <stop offset="1" stop-color="var(--teal-bottom)"/>
        </linearGradient>
        <linearGradient id="photo-fill" x1="0" y1="0" x2="1" y2="1">
          <stop offset="0" stop-color="var(--photo-dark)"/>
          <stop offset="0.6" stop-color="var(--photo-light)"/>
          <stop offset="1" stop-color="var(--photo-dark)"/>
        </linearGradient>
        <linearGradient id="silver-fill" x1="0" y1="0" x2="1" y2="0">
          <stop offset="0" stop-color="var(--silver-light)"/>
          <stop offset="0.55" stop-color="var(--silver-dark)"/>
          <stop offset="1" stop-color="var(--silver-light)"/>
        </linearGradient>
        <linearGradient id="footer-band-fill" x1="0" y1="0" x2="1" y2="0">
          <stop offset="0" stop-color="var(--teal-bottom)"/>
          <stop offset="1" stop-color="var(--navy)"/>
        </linearGradient>
      </defs>
      <rect class="side-panel" x="0" y="0" width="271" height="900" fill="url(#side-panel-fill)"/>
      <g role="img" aria-label="Photo of a hand holding up a glowing holographic display of financial bar charts and data">
        <polygon class="hero-photo" points="271,0 632,0 632,335 271,437" fill="url(#photo-fill)"/>
      </g>
      <polygon class="silver-band" points="271,437 632,335 632,465 380,420" fill="url(#silver-fill)"/>
      <polygon class="footer-band" points="271,822 632,885 632,900 271,900" fill="url(#footer-band-fill)"/>
      <line class="panel-divider" x1="271" y1="0" x2="271" y2="900" stroke="#0a2c44" stroke-opacity="0.35" stroke-width="2"/>
    </svg>

    <header class="brand">
      <div class="brand-name">EVEN KEEL</div>
      <div class="brand-tagline">Financial Services</div>
    </header>

    <h1 class="headline">
      <span class="big">Are you a</span>
      <span class="small">small business</span>
      <span class="big">owner?</span>
    </h1>

    <p class="intro">
      Tradie or PAVC Service<br>
      Provider struggling to<br>
      stay on top of your<br>
      bookkeeping and<br>
      compliance obligations?<br>
      If so we would love to<br>
      help you get back on<br>
      track and take control of<br>
      your business finances so<br>
      that you can make<br>
      informed business<br>
      decisions and focus on<br>
      what you do best.
    </p>

    <ul class="services">
      <li>Accounts Payable | Accounts Receivable</li>
      <li>Customer Invoicing</li>
      <li>Bank and Credit Card Reconciliations</li>
      <li>Payroll | Superannuation | Payroll Tax</li>
      <li>Business Activity | Instalment Activity Statements</li>
      <li>Regular Financial Reports</li>
      <li>Ledgerly and Bookwise Set-Up and Training</li>
    </ul>
  </main>
</body>
</html>
```